Copper & Wren Labels*

Hello :) I am needing labels for my herbal tea/petal product. I am a small producer for the local restaurants (edible flowers/micro herbs & dried product). I am hoping to sell the dried product online. It will be sold in batches as it is ready so quite small/boutique and the label needs to be somewhat generic for the range of produce I make.
Feels: no/minimal plastic, product is in a reusable mason jar, we use organic/regenerative principles from soil health to end product. Treading gently on the land. High quality i.e only fresh hand picked leaf tips for the tea.

```html
<!DOCTYPE html>
<html lang="en">
<head>
<meta charset="utf-8">
<title>Copper &amp; Wren – Label Range</title>
<link rel="stylesheet" href="https://fonts.googleapis.com/css2?family=Playfair+Display:ital,wght@0,400;0,700;0,900;1,700;1,900&family=Montserrat:wght@700&display=swap">
<style>
  :root{
    --page:#ffffff;
    --paper:#e9e9e8;
    --paper-edge:#dcdcdb;
    --ink:#2b2a29;
    --rule:#7a7a78;
    --caption:#333333;
    --copper-light:#f0a679;
    --copper-dark:#b5602f;
    --green-light:#4fc46a;
    --green-dark:#0f6a2a;
  }
  *{box-sizing:border-box;margin:0;padding:0}
  html,body{width:1200px;height:1000px;overflow:hidden;background:var(--page)}
  .range{position:relative;width:1200px;height:1000px}

  .label{
    position:absolute;
    background:linear-gradient(160deg,#eeeeed 0%,var(--paper) 55%,var(--paper-edge) 100%);
    color:var(--ink);
  }
  .label__frame{position:absolute;inset:9px;border:1px solid var(--rule)}
  .caption{
    position:absolute;font-family:"Playfair Display",serif;font-size:12.5px;color:var(--caption);
  }

  /* brand mark */
  .brand{position:absolute;left:0;right:0;display:flex;flex-direction:column;align-items:center}
  .brand__dot{border-radius:50%;background:var(--ink)}
  .brand__dot--copper{background:radial-gradient(circle at 35% 30%,var(--copper-light),var(--copper-dark))}
  .brand__dot--green{background:radial-gradient(circle at 40% 35%,var(--green-light),var(--green-dark))}
  .brand__name{font-family:"Montserrat",sans-serif;font-weight:700;color:var(--ink);letter-spacing:.2px}

  .rule{position:absolute;left:50%;transform:translateX(-50%);height:1px;background:var(--rule)}

  .title{position:absolute;left:0;right:0;font-family:"Playfair Display",serif;color:var(--ink)}
  .title__first{display:block;font-weight:900;letter-spacing:-1px;line-height:1}
  .title__second{display:block;line-height:1}
  .title__amp{font-weight:400;font-size:.45em;margin-right:3px}
  .title__script{font-style:italic;font-weight:900}

  .tagline{position:absolute;left:0;right:0;text-align:center;font-family:"Playfair Display",serif;color:var(--ink)}
  .tagline__main{font-weight:700;display:block}
  .tagline__main small{font-size:.75em}
  .tagline__sub{font-weight:700;display:block}

  /* tall labels */
  .label--tall{width:193px;height:348px;top:313px}
  .label--tall .brand{top:31px}
  .label--tall .brand__dot{width:46px;height:46px}
  .label--tall .brand__name{font-size:12px;margin-top:3px}
  .label--tall .rule--top{top:102px;width:102px}
  .label--tall .title{top:142px;padding-left:24px}
  .label--tall .title__first{font-size:40px}
  .label--tall .title__second{font-size:52px;margin-top:-4px}
  .label--tall .rule--bottom{top:274px;width:102px}
  .label--tall .tagline{top:291px}
  .label--tall .tagline__main{font-size:11px}
  .label--tall .tagline__sub{font-size:7.6px;margin-top:2px}

  /* small label */
  .label--small{width:195px;height:233px;top:311px;left:724px}
  .label--small .brand{top:14px}
  .label--small .brand__dot{width:34px;height:34px}
  .label--small .brand__name{font-size:9px;margin-top:2px}
  .label--small .rule--top{top:67px;width:112px}
  .label--small .title{top:86px;padding-left:30px}
  .label--small .title__first{font-size:38px}
  .label--small .title__second{font-size:48px;margin-top:-4px}
  .label--small .rule--bottom{top:178px;width:112px}
  .label--small .tagline{top:192px}
  .label--small .tagline__main{font-size:9px}
  .label--small .tagline__sub{font-size:6.6px;margin-top:2px}

  /* info label */
  .label--info{width:194px;height:192px;top:314px;left:943px;font-family:"Playfair Display",serif}
  .info__heading{position:absolute;top:14px;left:0;right:0;text-align:center;font-size:11.5px;font-weight:700}
  .info__table{position:absolute;top:38px;left:4px;right:4px;border:1px solid var(--rule);border-collapse:collapse;font-size:10px}
  .info__table td{border:1px solid var(--rule);vertical-align:top;padding:6px 8px}
  .info__key{width:68px}
  .info__option{display:flex;align-items:center;gap:4px;line-height:16px}
  .info__option::before{content:"";width:9px;height:9px;border:1px solid var(--ink);border-radius:50%}
  .info__footer td{padding:4px 6px;font-size:9px}
  .info__origin{display:flex;align-items:center;gap:6px}
  .info__origin::before{content:"";width:12px;height:12px;border-radius:50%;background:var(--ink)}
</style>
</head>
<body>
<main class="range">

  <!-- black ink -->
  <section class="label label--tall" style="left:76px">
    <div class="label__frame"></div>
    <div class="brand"><span class="brand__dot"></span><span class="brand__name">fernhollow</span></div>
    <div class="rule rule--top"></div>
    <h1 class="title"><span class="title__first">copper</span><span class="title__second"><span class="title__amp">&amp;</span><span class="title__script">wren</span></span></h1>
    <div class="rule rule--bottom"></div>
    <p class="tagline"><span class="tagline__main">Grown, harvested <small>and</small> dried</span><span class="tagline__sub">Chemical free on our farm in the east ridge</span></p>
  </section>
  <p class="caption" style="left:76px;top:677px">5 x 9 cm - Black ink</p>

  <!-- copper foil -->
  <section class="label label--tall" style="left:291px">
    <div class="label__frame"></div>
    <div class="brand"><span class="brand__dot brand__dot--copper"></span><span class="brand__name">fernhollow</span></div>
    <div class="rule rule--top"></div>
    <h1 class="title"><span class="title__first">copper</span><span class="title__second"><span class="title__amp">&amp;</span><span class="title__script">wren</span></span></h1>
    <div class="rule rule--bottom"></div>
    <p class="tagline"><span class="tagline__main">Grown, harvested <small>and</small> dried</span><span class="tagline__sub">Chemical free on our farm in the east ridge</span></p>
  </section>
  <p class="caption" style="left:289px;top:677px">5 x 9 cm - Black ink + Copper foil</p>

  <!-- green foil -->
  <section class="label label--tall" style="left:507px">
    <div class="label__frame"></div>
    <div class="brand"><span class="brand__dot brand__dot--green"></span><span class="brand__name">fernhollow</span></div>
    <div class="rule rule--top"></div>
    <h1 class="title"><span class="title__first">copper</span><span class="title__second"><span class="title__amp">&amp;</span><span class="title__script">wren</span></span></h1>
    <div class="rule rule--bottom"></div>
    <p class="tagline"><span class="tagline__main">Grown, harvested <small>and</small> dried</span><span class="tagline__sub">Chemical free on our farm in the east ridge</span></p>
  </section>
  <p class="caption" style="left:506px;top:677px">5 x 9 cm -&nbsp; Black ink + Green foil</p>

  <!-- small front -->
  <section class="label label--small">
    <div class="brand"><span class="brand__dot"></span><span class="brand__name">fernhollow</span></div>
    <div class="rule rule--top"></div>
    <h1 class="title"><span class="title__first">copper</span><span class="title__second"><span class="title__amp">&amp;</span><span class="title__script">wren</span></span></h1>
    <div class="rule rule--bottom"></div>
    <p class="tagline"><span class="tagline__main">Grown, harvested <small>and</small> dried</span><span class="tagline__sub">Chemical free on our farm in the east ridge</span></p>
  </section>
  <p class="caption" style="left:724px;top:552px">5 x 6 cm - Black ink</p>

  <!-- info label -->
  <section class="label label--info">
    <h2 class="info__heading">Single Origin Herbal Tea</h2>
    <table class="info__table">
      <tr style="height:64px">
        <td class="info__key">Leaf Base:</td>
        <td>
          <span class="info__option">Lemon Verbena</span>
          <span class="info__option">Mint</span>
          <span class="info__option">Agastache</span>
        </td>
      </tr>
      <tr style="height:32px"><td class="info__key">Petals:</td><td></td></tr>
      <tr style="height:30px"><td class="info__key">Batch:</td><td></td></tr>
      <tr class="info__footer"><td colspan="2"><span class="info__origin">Tallow Creek&nbsp; - Victoria Australia</span></td></tr>
    </table>
  </section>
  <p class="caption" style="left:944px;top:518px">5 x 5 cm - Black ink</p>

</main>
</body>
</html>
```